Need Modern Elegant Professional Invoice Design

Need modern elegant professional invoice design along with a second page for time and expense log for professional services

```html
<!DOCTYPE html>
<html lang="en">
<head>
<meta charset="utf-8">
<title>Invoice – Kestrel Group</title>
<link href="https://fonts.googleapis.com/css2?family=Poppins:ital,wght@0,400;0,500;0,600;0,700;1,400&display=swap" rel="stylesheet">
<style>
  :root {
    --orange: #f5862a;
    --purple: #3b22b2;
    --ink: #141414;
    --row-grey: #ececec;
    --rule: #6b6a8c;
    --paper: #ffffff;
  }
  * { margin: 0; padding: 0; box-sizing: border-box; }
  html, body { width: 849px; height: 1200px; overflow: hidden; background: var(--paper); }
  body { font-family: "Poppins", sans-serif; color: var(--ink); position: relative; }

  .header-band {
    position: absolute; left: 0; top: 0; width: 373px; height: 154px;
    background: var(--orange); border-bottom-right-radius: 76px;
  }
  .invoice-title {
    position: absolute; left: 44px; top: 34px;
    font-size: 50px; font-weight: 700; color: #fff; line-height: 1; letter-spacing: -0.5px;
    border-bottom: 3px solid #fff; padding-bottom: 2px;
  }
  .invoice-number {
    position: absolute; left: 44px; top: 86px;
    font-size: 19px; color: var(--purple); line-height: 1.2;
  }

  .brand {
    position: absolute; right: 33px; top: 62px;
    display: flex; align-items: center; gap: 10px;
    font-size: 30px; font-weight: 600; color: var(--orange); line-height: 1; white-space: nowrap;
  }
  .brand-mark { width: 18px; height: 18px; border-radius: 50%; background: var(--orange); }

  .info-block { position: absolute; top: 192px; }
  .info-block h2 { font-size: 20px; font-weight: 500; line-height: 1.3; margin-bottom: 10px; }
  .info-block p { font-size: 11.5px; line-height: 24.5px; letter-spacing: 0.3px; }
  .invoice-to { left: 44px; }
  .bank-detail { left: 347px; }
  .total-due {
    position: absolute; left: 672px; top: 199px;
    font-size: 23px; font-weight: 500; line-height: 1.05; text-decoration: underline;
    text-underline-offset: 3px;
  }

  .items {
    position: absolute; left: 46px; top: 366px; width: 769px;
    border-collapse: collapse; table-layout: fixed;
  }
  .items th {
    background: var(--orange); color: var(--purple); height: 49px;
    font-size: 20px; font-weight: 500; text-align: center;
    border-left: 1px solid var(--rule);
  }
  .items th:first-child { border-left: none; text-align: right; padding-right: 2px; }
  .items th.desc { text-align: left; padding-left: 50px; }
  .items td {
    height: 89px; border-left: 1px solid var(--rule); border-bottom: 1px solid var(--rule);
    font-size: 14px; text-align: center; vertical-align: middle;
  }
  .items td.num { border-left: none; vertical-align: top; text-align: left; padding: 20px 0 0 33px; }
  .items tr.shaded td { background: var(--row-grey); }
  .items tr.shaded td.num { border-left: 1px solid var(--rule); }
  .items tr.shaded td:last-child { border-right: 1px solid var(--rule); }
  .items td.desc { text-align: left; vertical-align: top; padding: 14px 0 0 20px; }
  .item-name { font-size: 14px; font-weight: 500; line-height: 1.4; margin-bottom: 5px; }
  .item-note { font-size: 14px; font-style: italic; line-height: 16px; padding-left: 2px; }

  .summary {
    position: absolute; left: 471px; top: 772px; width: 344px; height: 105px;
    background: var(--orange); padding: 6px 0 0 117px; color: var(--purple);
  }
  .summary-row { display: flex; font-size: 17.5px; line-height: 31.5px; }
  .summary-row .label { width: 102px; }
  .summary-row.grand { font-weight: 600; }

  .payment { position: absolute; left: 44px; top: 876px; }
  .payment h2, .terms h2 { font-size: 20px; font-weight: 500; line-height: 1.4; margin-bottom: 10px; }
  .payment p { font-size: 14px; line-height: 21px; }

  .terms { position: absolute; left: 44px; top: 1010px; }
  .terms p { font-size: 14px; font-style: italic; line-height: 33px; }

  .signature {
    position: absolute; left: 593px; top: 1010px; width: 188px; text-align: center;
    border-top: 2px solid var(--ink); padding-top: 4px;
  }
  .signature .name { font-size: 20px; font-weight: 500; line-height: 1.3; }
  .signature .role { font-size: 14px; line-height: 1.3; color: #333; }
</style>
</head>
<body>
  <div class="header-band"></div>
  <h1 class="invoice-title">INVOICE</h1>
  <div class="invoice-number">No : 1234 5678</div>

  <div class="brand"><span class="brand-mark"></span>Kestrel Group</div>

  <section class="info-block invoice-to">
    <h2>Invoice to</h2>
    <p>Adress &nbsp;&nbsp;&nbsp;&nbsp;&nbsp; : City anywhere</p>
    <p>Website : www.company.com</p>
    <p>Phone &nbsp;&nbsp;&nbsp; : 0123 456 789</p>
  </section>

  <section class="info-block bank-detail">
    <h2>Bank Detail</h2>
    <p>Bank Name : New Your Bank</p>
    <p>A/C Name &nbsp;&nbsp; : www.company.com</p>
    <p>Account no &nbsp;: 0123-456789</p>
  </section>

  <div class="total-due">Total due :<br>USD $510,00</div>

  <table class="items">
    <colgroup>
      <col style="width:67px"><col style="width:358px"><col style="width:136px"><col style="width:84px"><col style="width:124px">
    </colgroup>
    <thead>
      <tr><th>No.</th><th class="desc">Item Description</th><th>Unit Price</th><th>Qty</th><th>Total</th></tr>
    </thead>
    <tbody>
      <tr class="shaded">
        <td class="num">01.</td>
        <td class="desc"><div class="item-name">Item 1</div><div class="item-note">Nullam eleifend pharetra felis.<br>Mauris nibh velit, tristique ac,</div></td>
        <td>$100</td><td>1</td><td>$100</td>
      </tr>
      <tr>
        <td class="num">02.</td>
        <td class="desc"><div class="item-name">Item 2</div><div class="item-note">Nullam eleifend pharetra felis.<br>Mauris nibh velit, tristique ac,</div></td>
        <td>$100</td><td>1</td><td>$100</td>
      </tr>
      <tr class="shaded">
        <td class="num">03.</td>
        <td class="desc"><div class="item-name">Item 3</div><div class="item-note">Nullam eleifend pharetra felis.<br>Mauris nibh velit, tristique ac,</div></td>
        <td>$100</td><td>1</td><td>$100</td>
      </tr>
      <tr>
        <td class="num">04.</td>
        <td class="desc"><div class="item-name">Item 4</div><div class="item-note">Nullam eleifend pharetra felis.<br>Mauris nibh velit, tristique ac,</div></td>
        <td>$100</td><td>1</td><td>$100</td>
      </tr>
    </tbody>
  </table>

  <div class="summary">
    <div class="summary-row"><span class="label">Sub Total</span><span>: $500</span></div>
    <div class="summary-row"><span class="label">TAX</span><span>: $10</span></div>
    <div class="summary-row grand"><span>Grand Total: $510</span></div>
  </div>

  <section class="payment">
    <h2>Payment Method :</h2>
    <p>PayNest : payment@mail.com</p>
    <p>Card Payment We Accept : Vexa, Marlo Card</p>
  </section>

  <section class="terms">
    <h2>Term and Condition :</h2>
    <p>Aenean risus. Vestibulum scelerisque placerat sem.</p>
    <p>In eget sapien vitae massa rhoncus lacinia. Nullam at</p>
  </section>

  <div class="signature">
    <div class="name">Your Name</div>
    <div class="role">Marketing Officer</div>
  </div>
</body>
</html>
```